Norvane Builders Business Card

Modern and Professional Business Card for a Med size construction/development company.

See the samples below for the design I like … but I need ideas for incorporating the red company logo while still keeping the clean look of the card samples that are attached.

Logo and tag line on the back … info on the front.

Tagline: Quality Starts from the Ground Up

Target Market(s)

Med-Large General Contractors

Contact Information for Business Card

Norvane Builders Limited
42 Brenton Street
Elk Harbour, NL
B3K 7T2

t: 709-555-0147
f: 709-555-0192
w: www.norvanebuilders-example.com

Font styles to use
Sans Serif

Colors
fbee3e

Requirements
Must have
• I like the black and yellow designs of the attached samples …. but I'm not sure how to incorporate the red Norvane Builders logo into that design??
Nice to have
• Construction safety strips

```html
<!DOCTYPE html>
<html lang="en">
<head>
<meta charset="utf-8">
<title>Norvane Builders Business Card</title>
<link href="https://fonts.googleapis.com/css2?family=Open+Sans:wght@400;600;700&family=Oswald:wght@300;400&display=swap" rel="stylesheet">
<style>
  :root{
    --stage:#1f2225;
    --ink:#2a2a2a;
    --card-black:#262626;
    --card-white:#ffffff;
    --grey:#8c8c8c;
    --amber-light:#fdd54a;
    --amber:#fbb81a;
    --orange:#f7821b;
    --brand-red:#d9232a;
    --label:#f07b12;
  }
  *{box-sizing:border-box;margin:0;padding:0}
  html,body{width:1200px;height:900px;overflow:hidden;background:var(--stage)}
  body{font-family:"Open Sans",Arial,sans-serif;position:relative}
  .card{position:absolute;left:320px;width:560px;height:320px;border-radius:14px;overflow:hidden;background:var(--card-white);box-shadow:0 14px 30px rgba(0,0,0,.45)}
  .card--back{top:90px}
  .card--front{top:490px}
  .card svg.shapes{position:absolute;inset:0;width:100%;height:100%}

  /* back */
  .brand{position:absolute;display:flex;align-items:center;gap:10px}
  .brand__mark{width:26px;height:26px;background:var(--brand-red)}
  .brand__name{font-family:"Open Sans",Arial,sans-serif;font-weight:700;letter-spacing:1px;font-size:22px;line-height:1}
  .card--back .brand{left:240px;top:62px}
  .card--back .brand__name{color:var(--card-white)}
  .tagline{position:absolute;left:46px;top:258px;font-family:"Oswald",Arial,sans-serif;font-weight:300;font-size:19px;color:var(--ink);letter-spacing:.3px}

  /* front */
  .company{position:absolute;left:26px;top:26px;font-weight:700;font-size:17px;color:var(--ink)}
  .contact{position:absolute;left:26px;top:62px;list-style:none}
  .contact li{display:flex;align-items:center;gap:8px;font-size:11px;color:#fff;margin-bottom:8px}
  .contact svg{width:14px;height:14px;flex:none}
  .person{position:absolute;left:352px;top:44px}
  .person__name{font-weight:600;font-size:24px;color:#3a3a3a}
  .person__role{font-size:13px;color:var(--label);margin-top:2px}
  .person__rule{width:120px;height:2px;margin-top:6px;background:linear-gradient(90deg,#8a2a12,rgba(138,42,18,0))}
  .card--front .brand{left:250px;top:252px}
  .card--front .brand__name{color:var(--ink);font-size:18px}
</style>
</head>
<body>

<section class="card card--back" aria-label="Card back">
  <svg class="shapes" viewBox="0 0 560 320" preserveAspectRatio="none">
    <defs>
      <linearGradient id="amberBand" x1="0" y1="0" x2="1" y2="1">
        <stop offset="0" stop-color="var(--amber-light)"/>
        <stop offset="1" stop-color="var(--amber)"/>
      </linearGradient>
    </defs>
    <rect width="560" height="320" fill="var(--card-black)"/>
    <polygon points="0,130 60,150 120,205 175,190 200,225 280,238 330,205 400,222 560,220 560,320 0,320" fill="url(#amberBand)"/>
    <polygon points="0,145 55,165 115,215 175,205 200,240 280,248 330,222 400,236 560,232 560,320 0,320" fill="var(--card-white)"/>
  </svg>
  <div class="brand">
    <span class="brand__mark"></span>
    <span class="brand__name">NORVANE BUILDERS LIMITED</span>
  </div>
  <p class="tagline">Quality Starts from the Ground Up</p>
</section>

<section class="card card--front" aria-label="Card front">
  <svg class="shapes" viewBox="0 0 560 320" preserveAspectRatio="none">
    <defs>
      <linearGradient id="orangePanel" x1="1" y1="0" x2="0" y2="1">
        <stop offset="0" stop-color="var(--amber-light)"/>
        <stop offset=".55" stop-color="var(--amber)"/>
        <stop offset="1" stop-color="var(--orange)"/>
      </linearGradient>
    </defs>
    <rect width="560" height="320" fill="var(--card-white)"/>
    <polygon points="0,0 325,0 272,200 0,262" fill="url(#orangePanel)"/>
    <polygon points="0,262 272,200 250,218 0,282" fill="var(--grey)"/>
    <polygon points="325,0 346,0 300,222 250,218 272,200" fill="var(--card-black)"/>
    <polygon points="0,282 250,218 300,222 0,300" fill="var(--card-black)"/>
  </svg>

  <h1 class="company">Norvane Builders Limited</h1>
  <ul class="contact">
    <li><svg viewBox="0 0 14 14"><rect width="14" height="14" rx="2" fill="var(--ink)"/><path d="M7 3a3 3 0 0 1 3 3c0 2-3 5-3 5S4 8 4 6a3 3 0 0 1 3-3z" fill="#fff"/></svg>42 Brenton Street, Elk Harbour, NL, B3K 7T2</li>
    <li><svg viewBox="0 0 14 14"><rect width="14" height="14" rx="2" fill="var(--ink)"/><path d="M4 3h2l1 2-1.2 1a5 5 0 0 0 2.2 2.2L9 7l2 1v2a1 1 0 0 1-1 1A7 7 0 0 1 3 4a1 1 0 0 1 1-1z" fill="#fff"/></svg>709-555-0147
      <svg viewBox="0 0 14 14"><rect width="14" height="14" rx="2" fill="var(--ink)"/><rect x="3.5" y="4" width="7" height="6" fill="#fff"/><rect x="5" y="2.5" width="4" height="2" fill="#fff"/></svg>709-555-0192</li>
    <li><svg viewBox="0 0 14 14"><rect width="14" height="14" rx="2" fill="var(--ink)"/><rect x="3" y="4" width="8" height="6" fill="#fff"/><path d="M3 4l4 3 4-3" stroke="var(--ink)" fill="none"/></svg>info@norvanebuilders-example.com</li>
    <li><svg viewBox="0 0 14 14"><rect width="14" height="14" rx="2" fill="var(--ink)"/><circle cx="7" cy="7" r="3.6" fill="none" stroke="#fff"/><path d="M3.4 7h7.2M7 3.4v7.2" stroke="#fff"/></svg>www.norvanebuilders-example.com</li>
  </ul>

  <div class="person">
    <p class="person__name">Example Name</p>
    <p class="person__role">Designation</p>
    <div class="person__rule"></div>
  </div>

  <div class="brand">
    <span class="brand__mark"></span>
    <span class="brand__name">NORVANE BUILDERS LIMITED</span>
  </div>
</section>

</body>
</html>
```